Cloud-based Health 2.0 Web Site

We need the overall look and feel for a new cloud-based Health 2.0 web site where health professionals can manage and interact with their patients/clients.

The plan is to generate a landing page that can grab the attention of health professionals (doctors, nurses, personal trainers, etc...). This page should have an attractive "Sign Up for Free" or similar button/message, as well as a login section for users already registered. We currently have a view on having a number of messages displayed, either as a slider or as separate areas on the page (decision is up for grabs).

Secondly, we need a standard "framework" for all the other pages which will be accessible once the user has authenticated with a clean, airy and spacious feel. This will provide styling for standard elements (input boxes, checkboxes, etc...) as well as a given layout, possibly 3 columns (fixed-fluid-fixed) although we leave this to the designer's choice.

We want to stress the importance of the Cloud, as well as make users feel like "this is the place to be if you're a modern, tech savvy health professional". Also of high importance is to show that this is a secure place, where data is accessible from anywhere yet also highly protected.

This project is going to provide long-term work for the winner and possibly those we consider close runner ups, so if you guys are interested in grabbing our attention so you can become our designer of choice, this is your chance!

Standard pages we are looking to receive after the selection process:

* Landing page
* Health Professional Profile Page (personal details, professional details, photo...)
* Patient list / Patient Management page
* Patient profile (details, health details...)
* Generic "item" management page (item refers to documents, images, contacts, etc...)

The logo for the site/product is also up for grabs, and a bonus payment can be given if you provide one that both matches the style of the site whilst being one that could be reused for mobile app icons, etc...

The site name is "vornatik" (all lower-case) for those of you wanting to work on the logo part. As I said before, the logo should contain a component that could be use as the recognisable icon in a mobile phone app. Something that can be easily identified in both the site and the app that connects them together.

vornatik is made up of two parts (vorn + atik), and you might want to consider differentiating them by the use of colour, fonts or however you think appropriate.

New sample screen-shots of the existing functionality have been uploaded to help you mock up some screens.

PLEASE NOTE: This are to be used for content/widget design only! The layout of how these are represented, e.g. accordion, slider, tree, list... is entirely up to you! Don't guide your layout based on these screen-shots, unless you think they are the way to go, of course. 

We want your creative input, so please innovate! :)

Thanks!

Target Market(s)

Health Professionals

Industry/Entity Type

Health

Requirements
Must have
• * A landing page that grabs the users attention but is "different" from the rest of pages (although within the same design/style parameters)

* A generic page framework for the rest of the pages (style guide)
Nice to have
• A modern and clean logo to go with the site. If the logo is selected, this can result in a bonus payment to be decided.

```html
<!DOCTYPE html>
<html lang="en">
<head>
<meta charset="utf-8">
<title>vornatik – Personal Details</title>
<link href="https://fonts.googleapis.com/css2?family=Open+Sans:wght@400;600;700&family=Arimo:wght@400;700&display=swap" rel="stylesheet">
<style>
:root{
  --sky-top:#9fcdee;
  --sky-mid:#cfe6f7;
  --white:#ffffff;
  --brand-blue:#1b9ad6;
  --tab-blue-top:#1a98dc;
  --tab-blue-bottom:#0a5fa8;
  --tab-green-top:#9ad61c;
  --tab-green-bottom:#5faa0c;
  --ink:#1e1e1e;
  --label:#2a2a2a;
  --muted:#777777;
  --field-border:#c9c9c9;
  --panel-border:#e2e2e2;
  --footer-top:#6d6d6d;
  --footer-bottom:#2e2e2e;
  --photo-fill:#6b5a4e;
  --photo-dark:#1c1a19;
}
*{box-sizing:border-box;margin:0;padding:0}
html,body{width:1200px;height:916px;overflow:hidden}
body{font-family:"Arimo",Arial,sans-serif;color:var(--ink);background:var(--white)}
.canvas{position:relative;width:1200px;height:916px;overflow:hidden;
  background:linear-gradient(180deg,var(--sky-top) 0%,var(--sky-mid) 40%,#eaf4fb 58%,var(--white) 64%,var(--white) 100%)}
.sky-decor{position:absolute;left:0;top:0;width:1200px;height:566px;
  background:radial-gradient(ellipse at 50% 0%,rgba(255,255,255,.55) 0%,rgba(255,255,255,0) 55%)}
.abs{position:absolute}

/* header */
.brand{left:160px;top:44px;display:flex;align-items:center;gap:8px;
  font-family:"Open Sans",sans-serif;font-weight:700;font-size:34px;color:var(--brand-blue);letter-spacing:.5px}
.brand-dot{width:14px;height:14px;border-radius:50%;background:var(--brand-blue)}
.main-nav a{position:absolute;top:26px;font-family:"Open Sans",sans-serif;font-size:12.5px;color:#111;text-decoration:none}
.main-nav .active{left:513px;top:18px;width:80px;height:31px;border-radius:7px;border:2px solid #fff;
  background:linear-gradient(#fdfdfd,#d9dde0);display:flex;align-items:center;justify-content:center;
  box-shadow:0 1px 3px rgba(0,0,0,.25)}
.main-nav .sep{position:absolute;top:25px;font-size:13px;color:#111}
.auth-btn{top:90px;height:24px;border-radius:6px;background:linear-gradient(#ffffff,#dcdcdc);
  box-shadow:0 1px 2px rgba(0,0,0,.25);font-family:"Open Sans",sans-serif;font-size:12.5px;color:#444;
  display:flex;align-items:center;justify-content:center}

/* panel */
.panel{left:132px;top:137px;width:934px;height:661px;background:var(--white);border:1px solid var(--panel-border)}
.panel-shadow{left:150px;top:805px;width:900px;height:14px;border-radius:50%;
  background:radial-gradient(ellipse at center,rgba(0,0,0,.35) 0%,rgba(0,0,0,0) 70%)}
.tabs{left:134px;top:142px;width:929px;height:38px;border-radius:6px;display:flex;overflow:hidden;
  background:linear-gradient(var(--tab-blue-top),var(--tab-blue-bottom))}
.tab{height:38px;display:flex;align-items:center;justify-content:center;font-family:"Open Sans",sans-serif;
  font-size:13px;color:#fff;border-right:1px solid rgba(255,255,255,.35)}
.tab.current{width:141px;background:linear-gradient(var(--tab-green-top),var(--tab-green-bottom))}
.tab.w1{width:163px}
.tab.w2{width:152px;border-right:none}

/* form */
.field-label{left:160px;font-size:12px;font-weight:700;color:var(--label);letter-spacing:.5px;transform:translateY(-50%)}
.username{left:156px;top:234px;font-size:15px;font-weight:700;color:var(--brand-blue);letter-spacing:.6px}
.input{left:156px;width:205px;height:27px;border:1px solid var(--field-border);border-radius:14px;
  background:#fff;font-size:12px;color:#333;padding-left:9px;display:flex;align-items:center;letter-spacing:.3px}
.added-value{left:163px;top:676px;font-size:12px;color:#333;letter-spacing:.4px}
.save-btn{left:159px;top:718px;width:86px;height:32px;border-radius:16px;
  background:linear-gradient(#2a9be0,#0b58a6);box-shadow:2px 3px 3px rgba(0,0,0,.25);
  color:#fff;font-weight:700;font-size:17px;letter-spacing:2px;display:flex;align-items:center;justify-content:center}

/* photo card */
.photo-card{left:543px;top:194px;width:497px;height:187px;border:1px solid #ececec;
  background:linear-gradient(#ffffff,#efefef)}
.photo-card-shadow{left:560px;top:382px;width:468px;height:12px;border-radius:50%;
  background:radial-gradient(ellipse at center,rgba(0,0,0,.4) 0%,rgba(0,0,0,0) 70%)}
.card-title{left:556px;top:205px;font-size:15px;font-weight:700;color:var(--brand-blue);letter-spacing:1px}
.card-rule{left:556px;top:225px;width:390px;border-top:1px dotted #999}
.photo-frame{left:555px;top:234px;width:146px;height:137px;border:1px solid #ddd;background:#ececec}
.photo{left:562px;top:244px;width:131px;height:120px;
  background:radial-gradient(ellipse at 50% 55%,var(--photo-fill) 0%,#3a302a 60%,var(--photo-dark) 100%)}
.upload-text{left:711px;top:232px;font-size:15px;color:#333;letter-spacing:.3px}
.meta{left:711px;font-size:12px;color:var(--muted);letter-spacing:.3px}
.meta b{color:#666}
.pill{left:708px;width:119px;height:23px;border:1px solid #ddd;border-radius:12px;
  background:linear-gradient(#ffffff,#f0f0f0);font-size:12px;color:#333;display:flex;align-items:center;gap:6px;padding-left:0}
.pill svg{flex:none}
.back-link{left:974px;top:685px;font-size:12px;color:#555}

/* footer */
.footer{left:0;top:856px;width:1200px;height:60px;background:linear-gradient(var(--footer-top),var(--footer-bottom));
  display:flex;align-items:center;justify-content:center;font-family:"Open Sans",sans-serif;font-size:12.5px;color:#fff}
.footer span{margin:0 8px}
</style>
</head>
<body>
<div class="canvas">
  <div class="sky-decor" role="img" aria-label="Soft sky with drifting clouds and light rays"></div>

  <div class="abs brand"><span>vornatik</span><span class="brand-dot"></span></div>

  <nav class="main-nav">
    <a class="abs active" href="#">About us</a>
    <span class="sep" style="left:609px">|</span>
    <a href="#" style="left:648px">solutions</a>
    <span class="sep" style="left:736px">|</span>
    <a href="#" style="left:766px">Services</a>
    <span class="sep" style="left:844px">|</span>
    <a href="#" style="left:879px">News &amp; Events</a>
    <span class="sep" style="left:989px">|</span>
    <a href="#" style="left:1013px">Contact us</a>
  </nav>

  <div class="abs auth-btn" style="left:890px;width:66px">Login</div>
  <div class="abs auth-btn" style="left:966px;width:98px">Sign Up Now</div>

  <div class="abs panel-shadow"></div>
  <div class="abs panel"></div>

  <div class="abs tabs">
    <div class="tab current">Personal Details</div>
    <div class="tab w1">Current Treatments</div>
    <div class="tab w2">Medical History</div>
  </div>

  <div class="abs field-label" style="top:218px">Username</div>
  <div class="abs username">sample@clientbox.net</div>

  <div class="abs field-label" style="top:278px">Language Culture</div>
  <div class="abs input" style="top:294px">Spanish Espanol</div>

  <div class="abs field-label" style="top:343px">First name</div>
  <div class="abs input" style="top:357px;padding-left:6px">Renato</div>

  <div class="abs field-label" style="top:408px">Middelname</div>
  <div class="abs input" style="top:420px"></div>

  <div class="abs field-label" style="top:468px">Lastname</div>
  <div class="abs input" style="top:480px">Calveri</div>

  <div class="abs field-label" style="top:535px">Sex</div>
  <div class="abs input" style="top:547px">Male</div>

  <div class="abs field-label" style="top:597px">Date of birth</div>
  <div class="abs input" style="top:610px;padding-left:6px">13/1/197</div>

  <div class="abs field-label" style="top:658px">Added on</div>
  <div class="abs added-value">22/11/2011&nbsp;&nbsp; 23:30:48</div>

  <div class="abs save-btn">SAVE</div>

  <div class="abs photo-card-shadow"></div>
  <div class="abs photo-card"></div>
  <div class="abs card-title">PATIENT PHOTO</div>
  <div class="abs card-rule"></div>
  <div class="abs photo-frame"></div>
  <div class="abs photo" role="img" aria-label="Patient portrait photograph"></div>
  <div class="abs upload-text">Upload the patients's picture here.</div>
  <div class="abs meta" style="top:257px">Maximum SIze <b>4MB</b></div>
  <div class="abs meta" style="top:274px">Supported formats : <b>jPG, GIF or PNG</b></div>

  <div class="abs pill" style="top:300px">
    <svg width="23" height="23" viewBox="0 0 23 23"><circle cx="11.5" cy="11.5" r="10.5" fill="#6cc21c"/><path d="M11.5 6v11M6 11.5h11" stroke="#fff" stroke-width="3"/></svg>
    Change Photo
  </div>
  <div class="abs pill" style="top:334px">
    <svg width="23" height="23" viewBox="0 0 23 23"><circle cx="11.5" cy="11.5" r="10.5" fill="#a8141a"/><path d="M7.5 7.5l8 8M15.5 7.5l-8 8" stroke="#fff" stroke-width="3"/></svg>
    Remove Photo
  </div>

  <div class="abs back-link">&lt;&lt; Back to Patient</div>

  <footer class="abs footer">
    <span>About us |</span><span>Products &amp; solutions</span><span>|</span><span>Services</span><span>|</span><span>News &amp; Events</span><span>|</span><span>Regulatory &amp; Scientific</span>
  </footer>
</div>
</body>
</html>
```